Company PowerPoint Template to attract new customers

Looking for a set of template PowerPoint slides to use for my business. We sell a service where we sell products for brands. We need an Intro slide, slides that we can add text and images to and slides to show pricing. The slides do not need any 'content' as we have that - we just need something that looks attractive, and appealing. We want to draw people in and get them talking to us.

Target Market(s)

FMCG Businesses

Industry/Entity Type

FMCG Sales

Font styles to use
Sans Serif

Requirements
Must have
• A few variation of slide types

```html
<!DOCTYPE html>
<html lang="en">
<head>
<meta charset="utf-8">
<title>Vivid Parcel – Products Pitch Deck</title>
<link href="https://fonts.googleapis.com/css2?family=Poppins:wght@400;500;600;700;800&display=swap" rel="stylesheet">
<style>
:root{
  --pink:#EE3F66;
  --orange:#F7A01D;
  --brown:#4A2A10;
  --ink:#3d3d3d;
  --muted:#666;
  --stage:#A8A9AD;
  --white:#fff;
  --photo-a:linear-gradient(135deg,#e4e2df 0%,#a9a39c 55%,#5e5852 100%);
  --photo-b:linear-gradient(150deg,#cfd3d6 0%,#8d8f92 60%,#3f3b38 100%);
  --photo-c:linear-gradient(120deg,#d8c7b5 0%,#9a8a7c 55%,#4b4139 100%);
}
*{box-sizing:border-box}
html,body{margin:0;padding:0}
body{width:1200px;height:2266px;overflow:hidden;background:var(--stage);font-family:'Poppins',sans-serif;color:var(--ink)}
.canvas{position:relative;width:1200px;height:2266px}
.slide{position:absolute;background:var(--white);overflow:hidden;box-shadow:0 3px 8px rgba(0,0,0,.22)}
.slide.small{width:342px;height:192px}
.a{position:absolute;margin:0}
.photo{position:absolute;background:var(--photo-a)}
.photo.b{background:var(--photo-b)}
.photo.c{background:var(--photo-c)}
.title{position:absolute;margin:0;font-weight:700;text-transform:uppercase;color:var(--orange);line-height:1.08;letter-spacing:.2px}
.title .pink{color:var(--pink)}
.sub{position:absolute;margin:0;font-weight:700;font-size:7px;color:var(--brown)}
.sub.pink{color:var(--pink)}
.tiny{position:absolute;margin:0;font-size:3.6px;line-height:1.5;color:var(--muted)}
.label{position:absolute;margin:0;font-size:6.5px;font-weight:600;color:var(--brown)}
.footer-brand{position:absolute;left:12px;bottom:9px;display:flex;align-items:center;gap:2px;font-size:4.6px;font-weight:700;color:var(--orange)}
.footer-brand i{display:block;width:4px;height:4px;background:var(--pink)}
.page-no{position:absolute;right:12px;bottom:9px;font-size:4px;color:var(--muted)}
.dot{position:absolute;border-radius:50%;display:flex;align-items:center;justify-content:center;color:var(--white)}
.dot svg{width:55%;height:55%}
.dot.orange{background:var(--orange)}
.dot.pink{background:var(--pink)}
.dot.brown{background:var(--brown)}
.dot.outline{background:none;border:1.3px solid var(--pink);color:var(--brown)}
.ring{position:absolute;border-radius:50%;border-style:solid}
.btn{position:absolute;display:flex;align-items:center;justify-content:center;font-size:6px;font-weight:600;color:var(--white);text-transform:uppercase}
.idea-art{position:absolute;left:130px;top:52px;width:80px;height:112px;border-radius:40px 40px 12px 12px / 40px 40px 12px 12px;background:linear-gradient(135deg,var(--orange) 0%,var(--orange) 45%,var(--pink) 100%)}
/* hero */
.hero{left:65px;top:67px;width:1072px;height:602px}
.hero .corner{left:22px;top:20px;width:24px;height:24px;background:var(--pink)}
.brand{position:absolute;left:64px;top:92px;display:flex;align-items:center;gap:12px}
.brand i{display:block;width:22px;height:22px;background:var(--pink)}
.brand span{font-size:36px;font-weight:800;color:var(--orange);line-height:.95;letter-spacing:.5px}
.tagline{position:absolute;left:66px;top:165px;display:flex;align-items:center;gap:6px;font-size:14px;font-weight:600;color:var(--brown)}
.tagline b{display:block;width:40px;height:3px;background:var(--orange)}
.tagline b.pink{background:var(--pink)}
.hero-title{position:absolute;left:62px;top:246px;margin:0;font-size:92px;font-weight:700;color:var(--pink);line-height:1;letter-spacing:-1px}
.hero-sub{position:absolute;left:64px;top:348px;margin:0;font-size:50px;font-weight:700;color:var(--brown);line-height:1}
.hero-by{position:absolute;left:64px;top:424px;margin:0;font-size:23px;font-weight:700;color:var(--orange)}
.hero-copy{position:absolute;left:64px;top:458px;width:380px;margin:0;font-size:14px;line-height:1.45;color:#444}
.hero-arch-left{left:516px;top:0;width:251px;height:531px;border-radius:0 0 126px 126px}
.hero-bar{position:absolute;left:568px;top:553px;width:147px;height:15px;background:var(--orange)}
.hero-arch-right{left:788px;top:158px;width:252px;height:444px;border-radius:126px 126px 0 0}
.hero-dot{position:absolute;left:870px;top:106px;width:104px;height:104px;border-radius:50%;background:var(--pink);border:10px solid var(--white)}
.list{position:absolute;margin:0;padding:0;list-style:none;font-size:5px;color:var(--brown)}
.list li{border-bottom:.6px solid #ddd;padding:3.6px 0;width:126px}
.list li::before{content:"•";color:var(--pink);margin-right:2px}
.member{position:absolute;width:70px;text-align:center}
.member .face{width:40px;height:40px;border-radius:50%;margin:0 auto;background:var(--photo-c);border:2.5px solid var(--orange);border-top-color:var(--pink)}
.member h4{margin:4px 0 0;font-size:5.5px;color:var(--pink);font-weight:700}
.member h5{margin:0;font-size:4.5px;color:var(--brown);font-weight:600}
.member p{margin:2px 0 0;font-size:3.4px;line-height:1.5;color:var(--muted)}
.contact{position:absolute;left:222px;display:flex;align-items:center;gap:6px}
.contact .dot{position:relative;width:20px;height:20px;border:2px solid #fbd0da}
.contact p{margin:0;font-size:5px;line-height:1.3;color:var(--brown)}
.contact p b{font-weight:600}
</style>
</head>
<body>
<svg width="0" height="0" style="position:absolute" aria-hidden="true">
  <defs>
    <symbol id="i-gear" viewBox="0 0 24 24"><g fill="none" stroke="currentColor" stroke-width="2.4"><circle cx="12" cy="12" r="5"/><path d="M12 2v4M12 18v4M2 12h4M18 12h4M4.9 4.9l2.8 2.8M16.3 16.3l2.8 2.8M4.9 19.1l2.8-2.8M16.3 7.7l2.8-2.8"/></g></symbol>
    <symbol id="i-chart" viewBox="0 0 24 24"><g fill="currentColor"><rect x="4" y="13" width="4" height="7"/><rect x="10" y="8" width="4" height="12"/><rect x="16" y="4" width="4" height="16"/></g></symbol>
    <symbol id="i-doc" viewBox="0 0 24 24"><g fill="none" stroke="currentColor" stroke-width="2"><rect x="5" y="3" width="14" height="18" rx="2"/><path d="M8 8h8M8 12h8M8 16h5"/></g></symbol>
    <symbol id="i-screen" viewBox="0 0 24 24"><g fill="none" stroke="currentColor" stroke-width="2"><rect x="3" y="4" width="18" height="12" rx="1.5"/><path d="M9 20h6M12 16v4"/></g></symbol>
    <symbol id="i-chat" viewBox="0 0 24 24"><g fill="currentColor"><path d="M3 5h12v8H8l-3 3v-3H3z"/><path d="M17 9h4v8h-2v3l-3-3h-5v-2h6z"/></g></symbol>
    <symbol id="i-share" viewBox="0 0 24 24"><g fill="none" stroke="currentColor" stroke-width="2.2"><path d="M14 5l6 5-6 5"/><path d="M20 10h-7a7 7 0 0 0-7 7"/><path d="M4 7v13h13"/></g></symbol>
    <symbol id="i-org" viewBox="0 0 24 24"><g fill="currentColor"><rect x="9" y="3" width="6" height="5"/><rect x="2" y="16" width="6" height="5"/><rect x="9" y="16" width="6" height="5"/><rect x="16" y="16" width="6" height="5"/><path d="M11 8h2v3h7v5h-2v-3h-5v3h-2v-3H6v3H4v-5h7z"/></g></symbol>
    <symbol id="i-user" viewBox="0 0 24 24"><g fill="currentColor"><circle cx="12" cy="8" r="4"/><path d="M4 21a8 8 0 0 1 16 0z"/></g></symbol>
    <symbol id="i-search" viewBox="0 0 24 24"><g fill="none" stroke="currentColor" stroke-width="2.6"><circle cx="10" cy="10" r="6"/><path d="M15 15l6 6"/></g></symbol>
    <symbol id="i-coin" viewBox="0 0 24 24"><circle cx="12" cy="12" r="9" fill="currentColor"/><path d="M12 6v12M15 9h-4a2 2 0 0 0 0 4h2a2 2 0 0 1 0 4H9" fill="none" stroke="#EE3F66" stroke-width="2"/></symbol>
    <symbol id="i-phone" viewBox="0 0 24 24"><path fill="currentColor" d="M6.6 10.8a15 15 0 0 0 6.6 6.6l2.2-2.2a1 1 0 0 1 1-.25 11 11 0 0 0 3.6.6 1 1 0 0 1 1 1V20a1 1 0 0 1-1 1A17 17 0 0 1 3 4a1 1 0 0 1 1-1h3.5a1 1 0 0 1 1 1 11 11 0 0 0 .6 3.6 1 1 0 0 1-.25 1z"/></symbol>
    <symbol id="i-mail" viewBox="0 0 24 24"><g fill="none" stroke="currentColor" stroke-width="2.2"><rect x="3" y="5" width="18" height="14" rx="1.5"/><path d="M3 6l9 7 9-7"/></g></symbol>
    <symbol id="i-home" viewBox="0 0 24 24"><path fill="currentColor" d="M12 3l10 9h-3v9h-5v-6h-4v6H5v-9H2z"/></symbol>
  </defs>
</svg>

<main class="canvas">

  <!-- Title slide -->
  <section class="slide hero">
    <div class="a corner"></div>
    <div class="brand"><i></i><span>VIVID<br>PARCEL</span></div>
    <div class="tagline"><b></b>From Shelf to Spotlight<b class="pink"></b></div>
    <h1 class="hero-title">Products</h1>
    <h2 class="hero-sub">Pitch Deck</h2>
    <h3 class="hero-by">Template By:</h3>
    <p class="hero-copy">Lorem Ipsum is simply dummy text of the printing and typesetting industry.</p>
    <div class="photo hero-arch-left" role="img" aria-label="Photo: two colleagues working at laptops on a white desk"></div>
    <div class="hero-bar"></div>
    <div class="photo b hero-arch-right" role="img" aria-label="Photo: business handshake over a desk with laptops and charts"></div>
    <div class="hero-dot"></div>
  </section>

  <!-- 2 Welcome -->
  <section class="slide small" style="left:65px;top:715px">
    <div class="ring" style="left:-40px;top:-40px;width:74px;height:74px;border-width:7px;border-color:var(--pink)"></div>
    <h2 class="title" style="left:38px;top:26px;font-size:14px">Welcome<br>Slide</h2>
    <p class="tiny" style="left:192px;top:26px;width:118px">Add a short note about your brand, your offer and the value you bring to each retail partner.</p>
    <div class="photo" style="left:38px;top:79px;width:170px;height:64px" role="img" aria-label="Photo: team working around a laptop in an office"></div>
    <div class="dot orange" style="left:202px;top:71px;width:84px;height:84px;border:4px solid #fff;flex-direction:column">
      <span style="font-size:26px;font-weight:700;line-height:1">01.</span>
      <span style="font-size:8px;font-weight:600;line-height:1.05;text-align:center">Business<br>Slide</span>
    </div>
    <div class="footer-brand"><i></i>VIVID PARCEL</div><span class="page-no">2</span>
  </section>

  <!-- 3 Agenda -->
  <section class="slide small" style="left:429px;top:715px">
    <div class="a" style="left:54px;top:38px;width:1.2px;height:104px;background:var(--brown)"></div>
    <p class="a" style="left:63px;top:44px;font-size:8.5px;font-weight:500;color:var(--orange);line-height:1.3">HERE<br>GOES OF YOUR</p>
    <h2 class="title" style="left:63px;top:72px;font-size:14px;color:var(--pink)">Agenda</h2>
    <p class="tiny" style="left:63px;top:96px;width:80px">Use this space to outline the flow of the deck and the key points you will cover today.</p>
    <ul class="list" style="left:170px;top:33px">
      <li>Introduction</li><li>About Us</li><li>Company Profile</li><li>Team</li><li>Info graphic</li><li>Contact Us</li>
    </ul>
    <div class="footer-brand"><i></i>VIVID PARCEL</div><span class="page-no">3</span>
  </section>

  <!-- 4 About -->
  <section class="slide small" style="left:795px;top:715px">
    <div class="photo" style="left:-36px;top:-50px;width:190px;height:210px;border-radius:50%;border:4px solid var(--orange)" role="img" aria-label="Photo: team meeting around a conference table"></div>
    <div class="dot pink" style="left:114px;top:132px;width:20px;height:20px;border:3px solid #fff"></div>
    <h2 class="title" style="left:166px;top:32px;font-size:13px">About<br>Company</h2>
    <p class="sub pink" style="left:166px;top:66px;font-size:8px;font-weight:600">Creative Presentation</p>
    <div class="a" style="left:166px;top:79px;width:150px;height:.6px;background:#ccc"></div>
    <p class="tiny" style="left:166px;top:84px;width:150px">A few lines to introduce the company, the brands you represent and the results you deliver on shelf.</p>
    <p class="tiny" style="left:166px;top:117px;width:150px">A few lines on how the team works with buyers and distributors to grow sales across each channel.</p>
    <div class="footer-brand"><i></i>VIVID PARCEL</div><span class="page-no">4</span>
  </section>

  <!-- 5 -->
  <section class="slide small" style="left:65px;top:935px">
    <div class="ring" style="left:298px;top:-42px;width:84px;height:84px;border-width:10px;border-color:var(--pink)"></div>
    <h2 class="title" style="left:40px;top:35px;font-size:13.5px">Creative<br>Corporate<br>Design</h2>
    <p class="sub" style="left:40px;top:100px">Creative Presentation</p>
    <p class="tiny" style="left:40px;top:111px;width:88px">A short paragraph that explains this section of the offer in simple words.</p>
    <div class="dot brown" style="left:172px;top:30px;width:24px;height:24px"><svg><use href="#i-gear"/></svg></div>
    <p class="tiny" style="left:203px;top:31px;width:100px">Short line on the first key point of the service offer.</p>
    <p class="tiny" style="left:170px;top:83px;width:100px;text-align:right">Short line on the second key point of the offer.</p>
    <div class="dot orange" style="left:275px;top:80px;width:24px;height:24px"><svg><use href="#i-screen"/></svg></div>
    <div class="dot pink" style="left:172px;top:130px;width:24px;height:24px"><svg><use href="#i-gear"/></svg></div>
    <p class="tiny" style="left:203px;top:131px;width:100px">Short line on the third key point of the offer.</p>
    <div class="footer-brand"><i></i>VIVID PARCEL</div><span class="page-no">5</span>
  </section>

  <!-- 6 -->
  <section class="slide small" style="left:429px;top:935px">
    <div class="photo b" style="left:78px;top:20px;width:58px;height:58px;border-radius:50%" role="img" aria-label="Photo: hands typing on a laptop"></div>
    <div class="photo" style="left:22px;top:70px;width:48px;height:48px;border-radius:50%" role="img" aria-label="Photo: group working at a table"></div>
    <div class="photo c" style="left:80px;top:105px;width:54px;height:54px;border-radius:50%" role="img" aria-label="Photo: presenter at a whiteboard"></div>
    <h2 class="title" style="left:164px;top:28px;font-size:11.5px">Creative Corporate<br>Design</h2>
    <div class="dot outline" style="left:164px;top:69px;width:26px;height:26px"><svg><use href="#i-doc"/></svg></div>
    <div class="dot outline" style="left:200px;top:69px;width:26px;height:26px"><svg><use href="#i-screen"/></svg></div>
    <div class="dot outline" style="left:236px;top:69px;width:26px;height:26px"><svg><use href="#i-gear"/></svg></div>
    <p class="sub pink" style="left:164px;top:111px;font-size:7px">Creative Presentation</p>
    <p class="tiny" style="left:164px;top:122px;width:155px">A short paragraph that explains this part of the service and how it helps your brand partners sell more.</p>
    <div class="footer-brand"><i></i>VIVID PARCEL</div><span class="page-no">6</span>
  </section>

  <!-- 7 -->
  <section class="slide small" style="left:795px;top:935px">
    <div class="ring" style="left:-24px;top:20px;width:60px;height:60px;border-width:7px;border-color:var(--pink)"></div>
    <div class="ring" style="left:52px;top:-20px;width:40px;height:40px;border-width:6px;border-color:var(--pink)"></div>
    <div class="photo" style="left:22px;top:22px;width:150px;height:80px;border-radius:10px" role="img" aria-label="Photo: smiling team gathered around a laptop"></div>
    <div class="dot orange" style="left:31px;top:117px;width:12px;height:12px;border-radius:2px"><svg><use href="#i-chart"/></svg></div>
    <p class="label" style="left:47px;top:116px;font-size:5.5px;line-height:1.1">Project<br>Presentation</p>
    <p class="tiny" style="left:94px;top:116px;width:80px">Short line about a project and its outcome.</p>
    <div class="a" style="left:31px;top:142px;width:11px;height:11px;color:var(--pink)"><svg width="11" height="11"><use href="#i-user"/></svg></div>
    <p class="label" style="left:47px;top:142px;font-size:5.5px;line-height:1.1">Happy<br>Customer</p>
    <p class="tiny" style="left:94px;top:142px;width:80px">Short line about a happy client result.</p>
    <h2 class="title" style="left:198px;top:40px;font-size:13.5px">Creative<br>Corporate<br>Design</h2>
    <p class="tiny" style="left:198px;top:124px;width:115px">A short paragraph for this slide that gives a little more detail on the offer.</p>
    <div class="ring" style="left:302px;top:152px;width:70px;height:70px;border-width:9px;border-color:var(--orange)"></div>
    <div class="footer-brand"><i></i>VIVID PARCEL</div><span class="page-no">7</span>
  </section>

  <!-- 8 -->
  <section class="slide small" style="left:65px;top:1155px">
    <div class="photo b" style="left:0;top:0;width:46px;height:158px" role="img" aria-label="Photo: glass office tower"></div>
    <div class="ring" style="left:34px;top:138px;width:24px;height:24px;border-width:3px;border-color:var(--pink);background:#fff"></div>
    <h2 class="title" style="left:65px;top:44px;font-size:12px">Creative<br>Corporate<br>Design</h2>
    <p class="sub" style="left:65px;top:97px">Creative Presentation</p>
    <p class="tiny" style="left:65px;top:108px;width:90px">A short paragraph that explains this section of the offer in simple words.</p>
    <div class="ring" style="left:200px;top:-50px;width:190px;height:190px;border-width:12px;border-color:var(--orange);clip-path:inset(0 0 50% 50%)"></div>
    <div class="ring" style="left:270px;top:60px;width:120px;height:120px;border-width:12px;border-color:var(--orange);clip-path:inset(40% 0 0 50%)"></div>
    <div class="photo c" style="left:198px;top:33px;width:96px;height:130px;border-radius:12px" role="img" aria-label="Photo: engineer reviewing a tablet in a workshop"></div>
    <div class="footer-brand"><i></i>VIVID PARCEL</div><span class="page-no">8</span>
  </section>

  <!-- 9 Report bar chart -->
  <section class="slide small" style="left:429px;top:1155px">
    <h2 class="title" style="left:19px;top:14px;font-size:11.5px">Company<br><span class="pink">Report Design</span></h2>
    <p class="tiny" style="left:19px;top:44px;width:300px">Add a short summary of the sales figures shown in the chart below for each category this year.</p>
    <svg class="a" style="left:0;top:0" width="342" height="192" viewBox="0 0 342 192" aria-label="Bar chart of three series across four categories">
      <text x="175" y="72" font-size="4" fill="#777" text-anchor="middle" font-family="Poppins,sans-serif">Chart Title</text>
      <g stroke="#e5e5e5" stroke-width=".5"><line x1="50" y1="165" x2="300" y2="165"/><line x1="50" y1="149" x2="300" y2="149"/><line x1="50" y1="133" x2="300" y2="133"/><line x1="50" y1="117" x2="300" y2="117"/><line x1="50" y1="101" x2="300" y2="101"/><line x1="50" y1="85" x2="300" y2="85"/></g>
      <g font-size="3" fill="#888" font-family="Poppins,sans-serif"><text x="45" y="166">0</text><text x="45" y="150">1</text><text x="45" y="134">2</text><text x="45" y="118">3</text><text x="45" y="102">4</text><text x="45" y="86">5</text></g>
      <g fill="#F7A01D"><rect x="66" y="96" width="10" height="69"/><rect x="127" y="125" width="10" height="40"/><rect x="188" y="109" width="10" height="56"/><rect x="249" y="93" width="10" height="72"/></g>
      <g fill="#EE3F66"><rect x="78" y="127" width="10" height="38"/><rect x="139" y="95" width="10" height="70"/><rect x="200" y="136" width="10" height="29"/><rect x="261" y="120" width="10" height="45"/></g>
      <g fill="#4A2A10"><rect x="90" y="133" width="10" height="32"/><rect x="151" y="133" width="10" height="32"/><rect x="212" y="117" width="10" height="48"/><rect x="273" y="85" width="10" height="80"/></g>
      <g font-size="3" fill="#888" text-anchor="middle" font-family="Poppins,sans-serif"><text x="83" y="172">Category 1</text><text x="144" y="172">Category 2</text><text x="205" y="172">Category 3</text><text x="266" y="172">Category 4</text><text x="175" y="178">■ Series 1 ■ Series 2 ■ Series 3</text></g>
    </svg>
    <div class="footer-brand"><i></i>VIVID PARCEL</div><span class="page-no">9</span>
  </section>

  <!-- 10 Report line charts -->
  <section class="slide small" style="left:795px;top:1155px">
    <h2 class="title" style="left:16px;top:18px;font-size:11.5px">Company<br><span class="pink">Report Design</span></h2>
    <div class="a" style="left:37px;top:63px;width:.8px;height:104px;background:var(--brown)"></div>
    <div class="dot pink" style="left:35px;top:66px;width:5px;height:5px"></div>
    <p class="label" style="left:47px;top:63px">Title one</p>
    <p class="tiny" style="left:47px;top:72px;width:80px">Short note on the first result shown here.</p>
    <div class="dot pink" style="left:35px;top:100px;width:5px;height:5px"></div>
    <p class="label" style="left:47px;top:97px">Title Two</p>
    <p class="tiny" style="left:47px;top:106px;width:80px">Short note on the second result shown here.</p>
    <div class="dot pink" style="left:35px;top:135px;width:5px;height:5px"></div>
    <p class="label" style="left:47px;top:132px">Title Three</p>
    <p class="tiny" style="left:47px;top:141px;width:80px">Short note on the third result shown here.</p>
    <svg class="a" style="left:160px;top:22px" width="170" height="150" viewBox="0 0 170 150" aria-label="Two line charts comparing series">
      <g font-size="3.5" fill="#777" font-family="Poppins,sans-serif" text-anchor="middle"><text x="90" y="5">Chart Title</text><text x="90" y="80">Chart Title</text></g>
      <g stroke="#e5e5e5" stroke-width=".5"><line x1="20" y1="12" x2="155" y2="12"/><line x1="20" y1="24" x2="155" y2="24"/><line x1="20" y1="36" x2="155" y2="36"/><line x1="20" y1="48" x2="155" y2="48"/><line x1="20" y1="88" x2="155" y2="88"/><line x1="20" y1="100" x2="155" y2="100"/><line x1="20" y1="112" x2="155" y2="112"/><line x1="20" y1="124" x2="155" y2="124"/></g>
      <polyline points="30,26 70,36 110,30 145,16" fill="none" stroke="#EE3F66" stroke-width="1"/>
      <polyline points="30,40 70,30 110,38 145,34" fill="none" stroke="#F7A01D" stroke-width="1"/>
      <polyline points="30,44 70,40 110,36 145,18" fill="none" stroke="#4A2A10" stroke-width="1"/>
      <polyline points="30,102 70,112 110,106 145,92" fill="none" stroke="#EE3F66" stroke-width="1"/>
      <polyline points="30,116 70,106 110,114 145,110" fill="none" stroke="#F7A01D" stroke-width="1"/>
      <polyline points="30,120 70,116 110,112 145,94" fill="none" stroke="#4A2A10" stroke-width="1"/>
      <g font-size="2.6" fill="#999" font-family="Poppins,sans-serif" text-anchor="middle"><text x="30" y="55">Category 1</text><text x="70" y="55">Category 2</text><text x="110" y="55">Category 3</text><text x="145" y="55">Category 4</text><text x="30" y="131">Category 1</text><text x="70" y="131">Category 2</text><text x="110" y="131">Category 3</text><text x="145" y="131">Category 4</text></g>
    </svg>
    <div class="footer-brand"><i></i>VIVID PARCEL</div><span class="page-no">10</span>
  </section>

  <!-- 11 -->
  <section class="slide small" style="left:65px;top:1375px">
    <h2 class="title" style="left:31px;top:36px;font-size:13.5px">Creative<br>Corporate<br>Design</h2>
    <p class="sub" style="left:31px;top:104px">Creative Presentation</p>
    <p class="tiny" style="left:31px;top:115px;width:95px">A short paragraph that explains this section of the offer in simple words.</p>
    <div class="dot orange" style="left:161px;top:25px;width:36px;height:36px"><svg><use href="#i-org"/></svg></div>
    <div class="dot pink" style="left:161px;top:73px;width:36px;height:36px"><svg><use href="#i-chat"/></svg></div>
    <div class="dot brown" style="left:161px;top:121px;width:36px;height:36px"><svg><use href="#i-share"/></svg></div>
    <div class="a" style="left:211px;top:23px;width:.8px;height:136px;background:var(--brown)"></div>
    <p class="label" style="left:219px;top:30px">Title one</p>
    <p class="tiny" style="left:219px;top:40px;width:90px">Short note on this point of the service.</p>
    <p class="label" style="left:219px;top:78px">Title Two</p>
    <p class="tiny" style="left:219px;top:88px;width:90px">Short note on this point of the service.</p>
    <p class="label" style="left:219px;top:127px">Title Three</p>
    <p class="tiny" style="left:219px;top:137px;width:90px">Short note on this point of the service.</p>
    <div class="footer-brand"><i></i>VIVID PARCEL</div><span class="page-no">11</span>
  </section>

  <!-- 12 -->
  <section class="slide small" style="left:429px;top:1375px">
    <h2 class="title" style="left:29px;top:32px;font-size:14px">Creative<br>Corporate<br>Design</h2>
    <p class="sub" style="left:29px;top:104px">Creative Presentation</p>
    <p class="tiny" style="left:29px;top:115px;width:100px">A short paragraph that explains this section of the offer in simple words.</p>
    <div class="a" style="left:172px;top:20px;width:170px;height:154px;background:var(--pink)"></div>
    <div class="photo" style="left:140px;top:60px;width:66px;height:66px;border-radius:50%;border:3px solid #fff" role="img" aria-label="Photo: team celebrating in a meeting room"></div>
    <p class="label" style="left:232px;top:33px;color:#fff">Title one</p>
    <p class="tiny" style="left:232px;top:43px;width:90px;color:#fff">Short note on this point of the service.</p>
    <p class="label" style="left:232px;top:74px;color:#fff">Title Two</p>
    <p class="tiny" style="left:232px;top:84px;width:90px;color:#fff">Short note on this point of the service.</p>
    <p class="label" style="left:232px;top:115px;color:#fff">Title Three</p>
    <p class="tiny" style="left:232px;top:125px;width:90px;color:#fff">Short note on this point of the service.</p>
    <div class="footer-brand"><i></i>VIVID PARCEL</div><span class="page-no">12</span>
  </section>

  <!-- 13 -->
  <section class="slide small" style="left:795px;top:1375px">
    <div class="ring" style="left:200px;top:-22px;width:30px;height:30px;border-width:5px;border-color:var(--pink)"></div>
    <h2 class="title" style="left:18px;top:16px;font-size:11.5px">Creative Corporate<br>Design</h2>
    <div class="dot orange" style="left:22px;top:60px;width:28px;height:28px;border:2px solid #fde1b4"><svg><use href="#i-doc"/></svg></div>
    <div class="dot pink" style="left:75px;top:60px;width:28px;height:28px;border:2px solid #fbd0da"><svg><use href="#i-screen"/></svg></div>
    <div class="dot brown" style="left:128px;top:60px;width:28px;height:28px;border:2px solid #e0d3c8"><svg><use href="#i-gear"/></svg></div>
    <p class="a" style="left:20px;top:95px;font-size:3.8px;font-weight:700;color:var(--orange)">01. TEXT ONE</p>
    <p class="a" style="left:73px;top:95px;font-size:3.8px;font-weight:700;color:var(--pink)">02. TEXT TWO</p>
    <p class="a" style="left:126px;top:95px;font-size:3.8px;font-weight:700;color:var(--brown)">03. TEXT THREE</p>
    <p class="tiny" style="left:20px;top:101px;width:44px">Short note that explains this first point.</p>
    <p class="tiny" style="left:73px;top:101px;width:44px">Short note that explains this second point.</p>
    <p class="tiny" style="left:126px;top:101px;width:44px">Short note that explains this third point.</p>
    <div class="ring" style="left:192px;top:32px;width:128px;height:128px;border-width:8px;border-color:var(--orange);clip-path:inset(50% 0 0 55%)"></div>
    <div class="photo c" style="left:196px;top:36px;width:120px;height:120px;border-radius:50%" role="img" aria-label="Photo: colleagues discussing work at a laptop"></div>
    <div class="footer-brand"><i></i>VIVID PARCEL</div><span class="page-no">13</span>
  </section>

  <!-- 14 -->
  <section class="slide small" style="left:65px;top:1589px">
    <svg class="a" style="left:36px;top:23px" width="180" height="50" viewBox="0 0 180 50" aria-label="Progress rings at 50, 75 and 40 percent">
      <g fill="none" stroke-width="2.5">
        <circle cx="22" cy="22" r="17" stroke="#eee"/><circle cx="22" cy="22" r="17" stroke="#F7A01D" stroke-dasharray="53.4 106.8" transform="rotate(-90 22 22)"/>
        <circle cx="76" cy="22" r="17" stroke="#eee"/><circle cx="76" cy="22" r="17" stroke="#EE3F66" stroke-dasharray="80.1 106.8" transform="rotate(-90 76 22)"/>
        <circle cx="130" cy="22" r="17" stroke="#eee"/><circle cx="130" cy="22" r="17" stroke="#4A2A10" stroke-dasharray="42.7 106.8" transform="rotate(-90 130 22)"/>
      </g>
      <g font-size="8" font-weight="600" fill="#3d3d3d" text-anchor="middle" font-family="Poppins,sans-serif"><text x="22" y="25">50%</text><text x="76" y="25">75%</text><text x="130" y="25">40%</text></g>
    </svg>
    <p class="tiny" style="left:38px;top:70px;width:44px;text-align:center">Short note on this figure.</p>
    <p class="tiny" style="left:92px;top:70px;width:44px;text-align:center">Short note on this figure.</p>
    <p class="tiny" style="left:146px;top:70px;width:44px;text-align:center">Short note on this figure.</p>
    <div class="photo b" style="left:36px;top:97px;width:72px;height:60px;border-radius:6px" role="img" aria-label="Photo: modern office interior"></div>
    <div class="photo" style="left:121px;top:97px;width:72px;height:60px;border-radius:6px" role="img" aria-label="Photo: hands reviewing a tablet"></div>
    <h2 class="title" style="left:211px;top:26px;font-size:13.5px">Creative<br>Corporate<br>Design</h2>
    <p class="tiny" style="left:211px;top:100px;width:100px">A short paragraph that explains these figures and what they mean for your brand partners.</p>
    <p class="tiny" style="left:211px;top:130px;width:100px">One more line of support text for this slide.</p>
    <div class="footer-brand"><i></i>VIVID PARCEL</div><span class="page-no">14</span>
  </section>

  <!-- 15 -->
  <section class="slide small" style="left:429px;top:1589px">
    <div class="ring" style="left:128px;top:-22px;width:42px;height:42px;border-width:5px;border-color:var(--pink)"></div>
    <div class="ring" style="left:222px;top:176px;width:40px;height:40px;border-width:5px;border-color:var(--orange)"></div>
    <h2 class="title" style="left:28px;top:32px;font-size:14px">Creative<br>Corporate<br>Design</h2>
    <p class="sub pink" style="left:28px;top:114px;font-weight:600">Creative Presentation</p>
    <div class="dot brown" style="left:28px;top:128px;width:20px;height:20px;border:2px solid #e0d3c8"><svg><use href="#i-doc"/></svg></div>
    <div class="dot brown" style="left:52px;top:128px;width:20px;height:20px;border:2px solid #e0d3c8"><svg><use href="#i-screen"/></svg></div>
    <div class="dot brown" style="left:76px;top:128px;width:20px;height:20px;border:2px solid #e0d3c8"><svg><use href="#i-gear"/></svg></div>
    <p class="tiny" style="left:182px;top:38px;width:125px">A short paragraph that explains this part of the service and how it helps each brand grow.</p>
    <p class="tiny" style="left:182px;top:64px;width:125px">A second short paragraph with more detail on results, reach and the support you give partners.</p>
    <div class="btn" style="left:182px;top:132px;width:93px;height:15px;border-radius:8px;background:var(--brown)">Text Added Here</div>
    <div class="footer-brand"><i></i>VIVID PARCEL</div><span class="page-no">15</span>
  </section>

  <!-- 16 -->
  <section class="slide small" style="left:795px;top:1589px;background:var(--pink)">
    <div class="a" style="left:11px;top:12px;width:1px;height:60px;background:var(--orange)"></div>
    <p class="a" style="left:16px;top:12px;font-size:8px;font-weight:500;color:#fff;line-height:1.1">Creative<br>Presentation</p>
    <div class="photo" style="left:-30px;top:40px;width:180px;height:180px;border-radius:50%;background:#fff"></div>
    <div class="photo b" style="left:-20px;top:46px;width:165px;height:140px;border-radius:0 80px 80px 0" role="img" aria-label="Photo: team meeting in a bright lounge"></div>
    <div class="ring" style="left:128px;top:66px;width:26px;height:26px;border-width:4px;border-color:var(--orange);background:#fff"></div>
    <h2 class="title" style="left:188px;top:26px;font-size:15px;color:#fff">Creative<br>Corporate<br>Design</h2>
    <div class="btn" style="left:188px;top:107px;width:103px;height:16px;background:var(--orange)">Text Added Here</div>
    <div class="btn" style="left:188px;top:136px;width:103px;height:16px;background:var(--orange)">Text Added Here</div>
    <span class="page-no" style="color:#fff">16</span>
  </section>

  <!-- 17 Idea -->
  <section class="slide small" style="left:65px;top:1806px">
    <h2 class="title" style="left:16px;top:16px;font-size:12px">Creative Idea<br>Design</h2>
    <div class="idea-art" role="img" aria-label="Illustration: light bulb divided into four coloured sections with small icons"></div>
    <p class="label" style="left:89px;top:58px">Title Addd</p>
    <p class="tiny" style="left:56px;top:66px;width:68px;text-align:right">Short note on this idea point here.</p>
    <p class="label" style="left:216px;top:58px">Title Addd</p>
    <p class="tiny" style="left:216px;top:66px;width:68px">Short note on this idea point here.</p>
    <p class="label" style="left:89px;top:106px">Title Addd</p>
    <p class="tiny" style="left:56px;top:114px;width:68px;text-align:right">Short note on this idea point here.</p>
    <p class="label" style="left:216px;top:106px">Title Addd</p>
    <p class="tiny" style="left:216px;top:114px;width:68px">Short note on this idea point here.</p>
    <div class="footer-brand"><i></i>VIVID PARCEL</div><span class="page-no">17</span>
  </section>

  <!-- 18 Growth -->
  <section class="slide small" style="left:429px;top:1806px">
    <h2 class="title" style="left:16px;top:17px;font-size:12px">Company Groth<br>Design</h2>
    <svg class="a" style="left:100px;top:55px" width="220" height="110" viewBox="0 0 220 110" aria-label="Growth diagram of diamonds rising to an arrow">
      <rect x="24" y="44" width="24" height="24" fill="#EE3F66" transform="rotate(45 36 56)"/>
      <rect x="45" y="64" width="24" height="24" fill="#F7A01D" transform="rotate(45 57 76)"/>
      <rect x="66" y="34" width="24" height="24" fill="#F7A01D" transform="rotate(45 78 46)"/>
      <rect x="87" y="54" width="24" height="24" fill="#EE3F66" transform="rotate(45 99 66)"/>
      <path d="M108 40 L145 8 L139 4 L160 0 L156 21 L151 15 L118 50 Z" fill="#F7A01D"/>
      <use href="#i-chart" x="30" y="50" width="12" height="12" color="#fff"/>
      <use href="#i-coin" x="51" y="70" width="12" height="12" color="#fff"/>
      <use href="#i-search" x="72" y="40" width="12" height="12" color="#fff"/>
      <use href="#i-user" x="93" y="60" width="12" height="12" color="#fff"/>
      <use href="#i-gear" x="124" y="30" width="12" height="12" color="#fff"/>
    </svg>
    <p class="label" style="left:44px;top:82px">Title Addd</p>
    <p class="tiny" style="left:44px;top:90px;width:60px">Short note on this growth step.</p>
    <p class="label" style="left:133px;top:66px">Title Addd</p>
    <p class="tiny" style="left:133px;top:74px;width:60px">Short note on this growth step.</p>
    <p class="label" style="left:241px;top:45px">Title Addd</p>
    <p class="tiny" style="left:241px;top:53px;width:60px">Short note on this growth step.</p>
    <p class="label" style="left:122px;top:155px">Title Addd</p>
    <p class="tiny" style="left:122px;top:163px;width:70px">Short note on this growth step.</p>
    <p class="label" style="left:220px;top:130px">Title Addd</p>
    <p class="tiny" style="left:220px;top:138px;width:60px">Short note on this growth step.</p>
    <div class="footer-brand"><i></i>VIVID PARCEL</div><span class="page-no">18</span>
  </section>

  <!-- 19 Timeline -->
  <section class="slide small" style="left:795px;top:1806px">
    <h2 class="title" style="left:15px;top:16px;font-size:12px">Company Timeline<br>Design</h2>
    <svg class="a" style="left:0;top:0" width="342" height="192" viewBox="0 0 342 192" aria-label="Timeline with five steps">
      <line x1="73" y1="108" x2="270" y2="108" stroke="#4A2A10" stroke-width="1.5"/>
      <g fill="#4A2A10"><circle cx="73" cy="108" r="2.5"/><circle cx="122" cy="108" r="2.5"/><circle cx="171" cy="108" r="2.5"/><circle cx="220" cy="108" r="2.5"/><circle cx="270" cy="108" r="2.5"/></g>
      <g fill="#F7A01D"><path d="M64 95 h18 l-9 8z"/><path d="M162 95 h18 l-9 8z"/><path d="M261 95 h18 l-9 8z"/><path d="M113 121 h18 l-9 -8z"/><path d="M211 121 h18 l-9 -8z"/></g>
      <g fill="#EE3F66"><circle cx="73" cy="87" r="7"/><circle cx="171" cy="87" r="7"/><circle cx="270" cy="87" r="7"/><circle cx="122" cy="129" r="7"/><circle cx="220" cy="129" r="7"/></g>
      <g fill="#fff" font-size="7" font-weight="700" text-anchor="middle" font-family="Poppins,sans-serif"><text x="73" y="89.5">1</text><text x="171" y="89.5">3</text><text x="270" y="89.5">5</text><text x="122" y="131.5">2</text><text x="220" y="131.5">4</text></g>
    </svg>
    <p class="label" style="left:60px;top:57px">Title Addd</p><p class="tiny" style="left:48px;top:65px;width:50px;text-align:center">Short note on this step.</p>
    <p class="label" style="left:158px;top:57px">Title Addd</p><p class="tiny" style="left:146px;top:65px;width:50px;text-align:center">Short note on this step.</p>
    <p class="label" style="left:257px;top:57px">Title Addd</p><p class="tiny" style="left:245px;top:65px;width:50px;text-align:center">Short note on this step.</p>
    <p class="label" style="left:109px;top:139px">Title Addd</p><p class="tiny" style="left:97px;top:147px;width:50px;text-align:center">Short note on this step.</p>
    <p class="label" style="left:207px;top:139px">Title Addd</p><p class="tiny" style="left:195px;top:147px;width:50px;text-align:center">Short note on this step.</p>
    <div class="footer-brand"><i></i>VIVID PARCEL</div><span class="page-no">19</span>
  </section>

  <!-- 20 Phone -->
  <section class="slide small" style="left:65px;top:2024px">
    <div class="ring" style="left:120px;top:-56px;width:120px;height:120px;border-width:12px;border-color:#ececec"></div>
    <h2 class="title" style="left:23px;top:26px;font-size:13.5px">Creative<br>Corporate<br>Design</h2>
    <div class="a" style="left:22px;top:100px;width:.8px;height:48px;background:var(--pink)"></div>
    <p class="tiny" style="left:29px;top:100px;width:88px">A short paragraph that explains this section of the offer in simple words.</p>
    <p class="tiny" style="left:29px;top:130px;width:88px">One more short line of support text.</p>
    <div class="a" style="left:149px;top:17px;width:72px;height:142px;border-radius:10px;background:#222;padding:3px">
      <div class="photo c" style="position:relative;width:100%;height:100%;border-radius:8px" role="img" aria-label="Photo on phone screen: colleagues reviewing work together"></div>
    </div>
    <p class="a" style="left:241px;top:90px;font-size:5.5px;font-weight:700;color:var(--pink)">TITLE ADDD</p>
    <p class="tiny" style="left:241px;top:98px;width:75px">Short note on this app feature.</p>
    <p class="a" style="left:241px;top:128px;font-size:5.5px;font-weight:700;color:var(--pink)">TITLE ADDD</p>
    <p class="tiny" style="left:241px;top:136px;width:75px">Short note on this app feature.</p>
    <div class="footer-brand"><i></i>VIVID PARCEL</div><span class="page-no">20</span>
  </section>

  <!-- 21 Team -->
  <section class="slide small" style="left:429px;top:2024px">
    <h2 class="title" style="left:0;width:342px;top:20px;font-size:11.5px;text-align:center">Meet Our Team</h2>
    <p class="tiny" style="left:46px;top:35px;width:250px;text-align:center">A short line that introduces the team behind the service and the support each brand partner gets.</p>
    <div class="member" style="left:44px;top:72px"><div class="face" role="img" aria-label="Team member portrait"></div><h4>MEMBER NAME</h4><h5>Position</h5><p>P : 000 1234 5678<br>E : name@company.com<br>W : namewebsite.com</p></div>
    <div class="member" style="left:136px;top:72px"><div class="face" role="img" aria-label="Team member portrait"></div><h4>MEMBER NAME</h4><h5>Position</h5><p>P : 000 1234 5678<br>E : name@company.com<br>W : namewebsite.com</p></div>
    <div class="member" style="left:228px;top:72px"><div class="face" role="img" aria-label="Team member portrait"></div><h4>MEMBER NAME</h4><h5>Position</h5><p>P : 000 1234 5678<br>E : name@company.com<br>W : namewebsite.com</p></div>
    <div class="footer-brand"><i></i>VIVID PARCEL</div><span class="page-no">21</span>
  </section>

  <!-- 22 Thank you -->
  <section class="slide small" style="left:795px;top:2024px">
    <h2 class="a" style="left:36px;top:24px;font-size:16px;font-weight:700;color:var(--brown)">Thank You</h2>
    <p class="a" style="left:36px;top:45px;font-size:8.5px;font-weight:600;color:var(--pink)">Creative Business Design</p>
    <p class="a" style="left:20px;top:140px;font-size:26px;font-weight:800;color:var(--orange);line-height:1">VIVID<br>PARCEL</p>
    <div class="contact" style="top:64px"><div class="dot pink"><svg><use href="#i-phone"/></svg></div><p><b>Our Phone</b><br>+000 12345 6789</p></div>
    <div class="contact" style="top:100px"><div class="dot pink"><svg><use href="#i-mail"/></svg></div><p><b>Our Email</b><br>company@name.com</p></div>
    <div class="contact" style="top:136px"><div class="dot pink"><svg><use href="#i-home"/></svg></div><p><b>Our Website</b><br>www.website.com</p></div>
  </section>

</main>
</body>
</html>
```